Website design in Wordpress for Golf Simulator Center

We are opening a new golf simulator center in Copenhagen, and need a website design. We are using wordpress, and our site is https://fernway-putt.dk
We will need a design for the frontpage, and a design for subpages (which we will be reusing for all subpages).
Logo is as seen on the site, and our base color scheme is leaf green.
As text, take the text on the current website, or put some placeholder text in english.
Should be responsive and look good on both desktop and mobile.
Target Market(s)
Male, 18-60, golf players
Coding
Coded - Design and coding required
Number of Pages Required
2 page
Font styles to use
Look and feel

```html
<!DOCTYPE html>
<html lang="da">
<head>
<meta charset="utf-8">
<title>Fernway Putt – Golfsimulator i Valby</title>
<link href="https://fonts.googleapis.com/css2?family=Cabin:wght@400;500;600;700&display=swap" rel="stylesheet">
<style>
:root{
  --green:#0b7a1f;
  --green-dark:#06611a;
  --green-light:#2f9a2c;
  --teal:#1f9c8a;
  --ink:#1b1b1b;
  --muted:#555;
  --grey-bg:#f1f1f1;
  --footer:#2b2b2b;
  --footer-deep:#1f1f1f;
  --white:#fff;
  --yellow:#f2c318;
}
*{box-sizing:border-box;margin:0;padding:0}
html,body{width:1200px;height:4012px;overflow:hidden}
body{font-family:"Cabin",Arial,sans-serif;color:var(--ink);background:var(--white);font-size:15px;line-height:1.5}
section,header,footer{position:relative;width:1200px;overflow:hidden}
.btn{display:inline-block;background:var(--green);color:var(--white);font-weight:700;font-size:14px;letter-spacing:.5px;text-transform:uppercase;padding:14px 22px;border-radius:2px}
.btn-outline{background:var(--white);color:var(--green)}
.photo{display:block}

.topbar{height:44px;display:flex;align-items:center;gap:28px;padding-left:128px;font-size:12px;color:#333}
.topbar span{display:flex;align-items:center;gap:8px}
.dot-ic{width:18px;height:18px;border-radius:50%;background:var(--green);display:flex;align-items:center;justify-content:center}

.nav{height:116px;display:flex;align-items:center;padding:0 128px;border-top:1px solid #eee}
.brand{display:flex;align-items:center;gap:10px;font-weight:700;font-size:24px;color:var(--ink);letter-spacing:1px}
.brand-sq{width:22px;height:22px;background:var(--green)}
.menu{display:flex;gap:34px;margin-left:auto;margin-right:34px;font-size:15px;font-weight:500}
.menu li{list-style:none;display:flex;align-items:center;gap:8px}

.hero{height:552px;background:linear-gradient(90deg,#1c1f1d 0%,#3a3e3a 45%,#6b706a 70%,#2a2d2b 100%)}
.hero .photo{position:absolute;inset:0}
.hero-copy{position:absolute;left:128px;top:210px;color:var(--white);width:560px}
.hero-copy h1{font-size:50px;font-weight:700;line-height:1.1;margin-bottom:14px}
.hero-copy p{font-size:17px;margin-bottom:26px}
.slides{position:absolute;right:128px;top:222px;color:var(--white);font-size:14px;display:flex;flex-direction:column;gap:14px;align-items:flex-end}
.slides span{display:flex;align-items:center;gap:8px}
.slides .on::before{content:"";width:22px;height:2px;background:var(--white)}
.mouse{position:absolute;left:590px;top:460px;width:20px;height:32px;border:2px solid var(--white);border-radius:10px}
.mouse::after{content:"";position:absolute;left:7px;top:6px;width:2px;height:7px;background:var(--white)}

.intro{height:308px;text-align:center;padding-top:60px}
.intro h2{font-size:28px;font-weight:700;margin-bottom:18px}
.intro p{width:760px;margin:0 auto 12px;font-size:14px;color:#333}

.opening{height:380px}
.opening .bg{position:absolute;inset:0}
.opening .photo{position:absolute;left:132px;top:24px;width:376px;height:324px;background:linear-gradient(180deg,#d9ddd8 0%,#bfc4bd 55%,#4c8f3b 80%,#2d6b26 100%)}
.opening-copy{position:absolute;left:580px;top:96px;width:470px;color:var(--white)}
.opening-copy h3{font-size:26px;font-weight:700;margin-bottom:10px}
.opening-copy p{font-size:13px;margin-bottom:26px}
.form{display:flex;gap:14px}
.form .field{width:260px;height:38px;background:var(--white);border-radius:2px;font-size:12px;color:#999;padding:10px 12px}
.form .btn{background:var(--teal);padding:10px 24px;text-transform:none;font-weight:600;font-size:13px}

.simulator{height:680px;text-align:center;padding-top:80px}
.simulator h2{font-size:32px;font-weight:700;margin-bottom:14px}
.simulator p{width:760px;margin:0 auto;font-size:14px;color:#333}
.gallery{position:absolute;left:128px;top:220px;display:flex;gap:10px}
.gallery .photo{width:308px;height:286px}
.g1{background:linear-gradient(180deg,#5b5348 0%,#8c8a70 45%,#3d6e2e 100%)}
.g2{background:linear-gradient(180deg,#4a4339 0%,#9aa27e 45%,#3a6a2a 100%)}
.g3{background:linear-gradient(180deg,#3d3f3b 0%,#6f7b63 45%,#4d5a3f 100%)}

.promo{height:360px}
.promo .photo{position:absolute;inset:0;background:radial-gradient(circle at 62% 55%,#6dbf3a 0%,#3d9a22 35%,#1f6e14 75%,#154f0e 100%);clip-path:polygon(0 14%,100% 0,100% 100%,0 100%)}
.promo-copy{position:absolute;left:0;right:0;top:150px;text-align:center;color:var(--white)}
.promo-copy h2{font-size:28px;font-weight:700}
.promo-copy p{font-size:14px;margin-bottom:22px}

.membership{height:420px;background:var(--grey-bg)}
.membership h2{position:absolute;left:128px;top:70px;font-size:28px;font-weight:700}
.perks{position:absolute;left:128px;top:130px;list-style:none;font-size:14px}
.perks li{display:flex;align-items:center;gap:12px;margin-bottom:9px}
.membership .photo{position:absolute;left:666px;top:84px;width:412px;height:290px;background:linear-gradient(180deg,#cfd3cc 0%,#a9b89a 55%,#3f7a2e 100%)}
.badge{position:absolute;left:596px;top:114px;width:104px;height:104px;border-radius:50%;background:var(--yellow);display:flex;flex-direction:column;align-items:center;justify-content:center;font-weight:700;font-size:17px;line-height:1.1}
.badge small{font-size:11px;font-weight:500}

.blog{height:640px;text-align:center;padding-top:70px}
.blog h2{font-size:30px;font-weight:700}
.cards{position:absolute;left:128px;top:150px;display:flex;gap:34px;text-align:left}
.card{width:292px}
.card .photo{height:200px;margin-bottom:14px}
.b1{background:linear-gradient(180deg,#3b3d3a 0%,#6f7f5c 55%,#2f5d22 100%)}
.b2{background:linear-gradient(180deg,#2f3e2e 0%,#45704a 55%,#1e3d20 100%)}
.b3{background:linear-gradient(180deg,#c9cdc7 0%,#92a37f 55%,#3d6d2c 100%)}
.card time{font-size:11px;color:var(--muted)}
.card h4{font-size:19px;font-weight:700;line-height:1.25;margin-top:4px}
.card h4.u{text-decoration:underline}
.blog .btn{position:absolute;left:540px;top:520px}

.newsletter{height:120px;background:var(--green);display:flex;align-items:center;padding-left:140px;gap:54px;color:var(--white)}
.newsletter h3{font-size:22px;font-weight:700}
.newsletter .field{width:300px;height:36px;background:var(--white);border-radius:2px;font-size:12px;color:#999;padding:9px 12px}
.newsletter .btn{background:var(--teal);padding:9px 28px;text-transform:none;font-weight:600;font-size:13px}
.newsletter .form{gap:16px}

.footer{height:320px;background:var(--footer);color:#ddd;font-size:13px}
.footer .brand{position:absolute;left:128px;top:52px;color:var(--white);font-size:22px}
.contact{position:absolute;left:128px;top:120px;list-style:none}
.contact li{display:flex;gap:12px;margin-bottom:12px;line-height:1.35}
.cols{position:absolute;left:380px;top:56px;display:flex;gap:60px}
.cols h5{font-size:16px;color:var(--white);font-weight:700;margin-bottom:10px}
.cols li{list-style:none;line-height:1.75}
.col1{width:220px}.col2{width:200px}
.social{position:absolute;left:880px;top:186px;display:flex;gap:14px}
.social span{width:16px;height:16px;border-radius:50%;background:#ddd}
.copy{height:72px;background:var(--footer-deep);color:#ccc;font-size:12px;padding:28px 128px}
</style>
</head>
<body>

<header>
  <div class="topbar">
    <span><i class="dot-ic"><svg width="10" height="10" viewBox="0 0 24 24"><path fill="#fff" d="M6.6 10.8a15 15 0 0 0 6.6 6.6l2.2-2.2c.3-.3.7-.4 1-.2 1.1.4 2.3.6 3.6.6.6 0 1 .4 1 1V20c0 .6-.4 1-1 1A17 17 0 0 1 3 4c0-.6.4-1 1-1h3.5c.6 0 1 .4 1 1 0 1.3.2 2.5.6 3.6.1.3 0 .7-.2 1z"/></svg></i>+45 31 20 47 59</span>
    <span><i class="dot-ic"><svg width="10" height="10" viewBox="0 0 24 24"><path fill="#fff" d="M12 2a7 7 0 0 0-7 7c0 5 7 13 7 13s7-8 7-13a7 7 0 0 0-7-7zm0 9.5A2.5 2.5 0 1 1 12 6.5a2.5 2.5 0 0 1 0 5z"/></svg></i>Lindholm Allé 14, 2500 Valby</span>
  </div>
  <nav class="nav">
    <div class="brand"><i class="brand-sq"></i>FERNWAY PUTT</div>
    <ul class="menu">
      <li>Golf Simulator <svg width="10" height="6"><path d="M1 1l4 4 4-4" stroke="#333" fill="none" stroke-width="1.5"/></svg></li>
      <li>Events <svg width="10" height="6"><path d="M1 1l4 4 4-4" stroke="#333" fill="none" stroke-width="1.5"/></svg></li>
      <li>Ressourcer <svg width="10" height="6"><path d="M1 1l4 4 4-4" stroke="#333" fill="none" stroke-width="1.5"/></svg></li>
      <li>Om Os <svg width="10" height="6"><path d="M1 1l4 4 4-4" stroke="#333" fill="none" stroke-width="1.5"/></svg></li>
    </ul>
    <span class="btn">Book now</span>
  </nav>
</header>

<section class="hero">
  <div class="photo" role="img" aria-label="Golfer swinging in front of a simulator screen in a dark room"></div>
  <div class="hero-copy">
    <h1>Golfsimulator i Valby</h1>
    <p>Indendørs golftræning med 8 simulatorer i Valby. Spil golf indendørs i alt slags vejr, både driving range eller en fuld 18-hullers omgang.</p>
    <span class="btn">See more</span>
  </div>
  <div class="slides"><span class="on">01</span><span>02</span><span>03</span></div>
  <div class="mouse"></div>
</section>

<section class="intro">
  <h2>Golfsimulator i Valby åbner januar 2023</h2>
  <p>13 januar 2023 åbner vi vort golfsimulatorcenter i Valby med 8 simulatorer af typen Skyline S4. Vi glæder os til at byde velkommen til nye og gamle golfspillere. Hos os kan du øve alt i lige meget hvilket vejr, hele året rundt.</p>
  <p>Hver simulator giver dig et helt præcis aftryk af dit slag, så du kan se præcis hvad der sker på en virtuel driving range, eller på en af vores mange velkendte baner.</p>
  <p>En golfsimulator er både til professionelle golfspillere, som vil træne stenhårdt, men er også velegnet til begyndere, golfentusiaster og firmaer.</p>
</section>

<section class="opening">
  <svg class="bg" width="1200" height="380" viewBox="0 0 1200 380" aria-hidden="true">
    <polygon points="0,70 1200,30 1200,380 0,380" fill="var(--green)"/>
  </svg>
  <div class="photo" role="img" aria-label="Player practising a swing on a simulator mat"></div>
  <div class="opening-copy">
    <h3>Åbningsreception</h3>
    <p>We will hold an opening reception on 20 January 2023 from 4 p.m. More information will be available on this page continuously, and via our newsletter, which you can sign up for here. See also our event page. Stop by and try a few shots, get a free Friday beer or a soft drink and join a raffle for free playing time and other prizes.</p>
    <div class="form"><span class="field">Emailadresse</span><span class="btn">Jo Tak!</span></div>
  </div>
</section>

<section class="simulator">
  <h2>Simulator</h2>
  <p>Lorem ipsum dolor sit amet consectetur. Suspendisse nibh nullam adipiscing gravida. Pretium interdum tortor at aenean etiam ante. Facilisi nisl sem ipsum aliquam at. Interdum ac metus id convallis varius est in. Orci morbi aliquam consectetur rhoncus nunc aenean pellentesque vulputate et.</p>
  <div class="gallery">
    <div class="photo g1" role="img" aria-label="Simulator bay with projected fairway"></div>
    <div class="photo g2" role="img" aria-label="Row of simulator bays with green turf"></div>
    <div class="photo g3" role="img" aria-label="Simulator lounge with screen"></div>
  </div>
</section>

<section class="promo">
  <div class="photo" role="img" aria-label="Close-up of green golf grass with a ball"></div>
  <div class="promo-copy">
    <h2>Køb et opstartsmedlemsskab allerede nu!</h2>
    <p>Så sikrer du dig spil hele året.</p>
    <span class="btn btn-outline">Learn more</span>
  </div>
</section>

<section class="membership">
  <h2>Opstartsmedlemsskab</h2>
  <ul class="perks">
    <li><svg width="16" height="16" viewBox="0 0 16 16"><circle cx="8" cy="8" r="8" fill="var(--green)"/><path d="M4.5 8.2l2.3 2.3 4.7-4.8" stroke="#fff" stroke-width="1.8" fill="none"/></svg>Fast indtræden fra år dette (efter 1 februar 2023)</li>
    <li><svg width="16" height="16" viewBox="0 0 16 16"><circle cx="8" cy="8" r="8" fill="var(--green)"/><path d="M4.5 8.2l2.3 2.3 4.7-4.8" stroke="#fff" stroke-width="1.8" fill="none"/></svg>Nøglebrik inkluderet: Adgang 06:00 til 23:00</li>
    <li><svg width="16" height="16" viewBox="0 0 16 16"><circle cx="8" cy="8" r="8" fill="var(--green)"/><path d="M4.5 8.2l2.3 2.3 4.7-4.8" stroke="#fff" stroke-width="1.8" fill="none"/></svg>Slit timers spil inkluderet</li>
    <li><svg width="16" height="16" viewBox="0 0 16 16"><circle cx="8" cy="8" r="8" fill="var(--green)"/><path d="M4.5 8.2l2.3 2.3 4.7-4.8" stroke="#fff" stroke-width="1.8" fill="none"/></svg>Booking: til hver pris (normalpris 400,- )</li>
    <li><svg width="16" height="16" viewBox="0 0 16 16"><circle cx="8" cy="8" r="8" fill="var(--green)"/><path d="M4.5 8.2l2.3 2.3 4.7-4.8" stroke="#fff" stroke-width="1.8" fill="none"/></svg>Gyldigt frem til 31 august 2023</li>
  </ul>
  <div class="photo" role="img" aria-label="Simulator screen showing a virtual golf course"></div>
  <div class="badge">KUN 500,-<small>Normalpris 2000</small></div>
</section>

<section class="blog">
  <h2>Blog</h2>
  <div class="cards">
    <article class="card">
      <div class="photo b1" role="img" aria-label="Golfer training in a simulator bay"></div>
      <time>2022-08-04</time>
      <h4>Golf training on a simulator</h4>
    </article>
    <article class="card">
      <div class="photo b2" role="img" aria-label="Bar area with green lighting"></div>
      <time>2022-08-04</time>
      <h4 class="u">The bar and all simulators are ready!</h4>
    </article>
    <article class="card">
      <div class="photo b3" role="img" aria-label="Bright simulator room with projected course"></div>
      <time>2022-08-04</time>
      <h4>The first blow has been struck!</h4>
    </article>
  </div>
  <span class="btn">View more</span>
</section>

<section class="newsletter">
  <h3>Sign up for our newsletter!</h3>
  <div class="form"><span class="field">Emailadresse</span><span class="btn">Jo Tak!</span></div>
</section>

<footer class="footer">
  <div class="brand"><i class="brand-sq"></i>FERNWAY PUTT</div>
  <ul class="contact">
    <li><svg width="14" height="14" viewBox="0 0 24 24"><path fill="#ddd" d="M12 2a7 7 0 0 0-7 7c0 5 7 13 7 13s7-8 7-13a7 7 0 0 0-7-7zm0 9.5A2.5 2.5 0 1 1 12 6.5a2.5 2.5 0 0 1 0 5z"/></svg><span>Lindholm Allé 14<br>2500 Valby<br>CVR: 40718265</span></li>
    <li><svg width="14" height="14" viewBox="0 0 24 24"><path fill="#ddd" d="M6.6 10.8a15 15 0 0 0 6.6 6.6l2.2-2.2c.3-.3.7-.4 1-.2 1.1.4 2.3.6 3.6.6.6 0 1 .4 1 1V20c0 .6-.4 1-1 1A17 17 0 0 1 3 4c0-.6.4-1 1-1h3.5c.6 0 1 .4 1 1 0 1.3.2 2.5.6 3.6.1.3 0 .7-.2 1z"/></svg><span>+45 31 20 47 59</span></li>
    <li><svg width="14" height="14" viewBox="0 0 24 24"><circle cx="12" cy="12" r="9" fill="none" stroke="#ddd" stroke-width="2"/><path d="M12 7v5l3 2" stroke="#ddd" stroke-width="2" fill="none"/></svg><span>Åbent 10:00–22:00 man–søn</span></li>
  </ul>
  <div class="cols">
    <ul class="col1"><h5>Golf Simulator</h5><li>Åbningstider og priser</li><li>Find vej</li><li>Simulatorer</li><li>Anvendelsesmuligheder</li><li>Handelsbetingelser</li><li>Betingelser for medlemsskab</li></ul>
    <ul class="col2"><h5>Events</h5><li>Firmafest</li><li>Polterabend</li><li>Hyggeture</li></ul>
    <ul><h5>Om Os</h5><li>Kontakt os</li><li>Persondatapolitik</li><li>Blog</li><li>Golfordbogen</li></ul>
  </div>
  <div class="social" aria-label="Social media"><span></span><span></span><span></span><span></span><span></span></div>
</footer>

<div class="copy">Copyrights Fernway Putt ApS</div>

</body>
</html>
```